Business Card - high end, modern health care

Hey designers!

We need a double sided business card for the boutique, cutting edge physical therapy rehabilitation centre in Sydney's Northern Beaches.

With the most qualified physios in the area The Harbourline Motion Clinic does what other physiotherapy practices do not, we take our time with our patients giving them longer appointments, better physios and therefor faster results!

We guarantee that the service people receive at THMC will be unparalleled.

Hence we need a business card to reflect our modern, boutique, high end service. The final design needs to reflect that we are in a class of our own yet with the feel of beachside retreat.

Below I have attached our logo in both blue on white and white on blue. The exact colour is;
and the font that we have used in our logo is Tex Gyre Aventador.

I like the idea of the blue as the main colour as it is more eye catching and our signage onto the main road will be in this blue and in the interest of consistency across marketing the blue needs to be a part of the design. However I would appreciate a few designs onto a wooden background as this is a visual theme within the fitout of the practice.

The design needs to be of standard size (91x55mm).

Target Market(s)

We target people who have an end outcome in mind and those who have had poor experiences with other providers and ensure that everyone gets the care that they deserve with a premium service that is tailored to the individuals circumstances. As a premium service, the target market is highly educated, business and tech savvy with the additional target market of elderly people who have self funded their retirement and see value in paying for the best ongoing rehabilitation to maintain independence.

Industry/Entity Type

Physical Therapy

Contact Information for Business Card

Name, designation( Titled Musculoskeletal Physiotherapist... there will also be those in the company that have multiple designations ie 5 or 6 words long), phone number, email, facebook, instagram, address

Font styles to use
Sans Serif

Colors

Designer to choose colors to be used in the design.

Requirements
Must have
• Front - The logo as large as possible, blue or wooden theme, and all of the important details.
• Back - A blank space/lines on which to write appointment times (no "Appointment, date, time" etc.)
Nice to have
• facebook url
• logos for facebook and instagram
• Mini logos for the phone and email?

```html
<!DOCTYPE html>
<html lang="en">
<head>
<meta charset="utf-8">
<title>The Harbourline Motion Clinic — Business Card</title>
<link rel="stylesheet" href="https://fonts.googleapis.com/css2?family=Raleway:wght@400;500;700&display=swap">
<style>
  :root {
    --brand-blue: #0e56a5;
    --ink: #1a1a1a;
    --paper: #fbfbfb;
    --backdrop: #e9e7e4;
    --rule: #2a2a2a;
    --dash: #9a9a9a;
    --social-a: #1d8fd6;
    --social-b: #e0508a;
  }
  * { box-sizing: border-box; margin: 0; padding: 0; }
  html, body { width: 1200px; height: 1200px; overflow: hidden; }
  body {
    background: var(--backdrop);
    font-family: "Raleway", sans-serif;
    color: var(--ink);
    position: relative;
  }
  .card {
    position: absolute;
    width: 760px;
    height: 459px;
    box-shadow: 0 14px 30px rgba(0,0,0,0.18);
  }
  /* Logo side */
  .card--logo {
    left: 360px;
    top: 110px;
    background: var(--brand-blue);
    display: flex;
    align-items: center;
    justify-content: center;
  }
  .brand-lockup {
    display: flex;
    align-items: center;
    gap: 22px;
    color: #fff;
  }
  .brand-lockup__dot {
    width: 78px;
    height: 78px;
    border-radius: 50%;
    background: #fff;
    flex: none;
  }
  .brand-lockup__name {
    font-weight: 700;
    font-size: 40px;
    line-height: 1.08;
    letter-spacing: 0.06em;
    text-transform: uppercase;
  }
  /* Details side */
  .card--details {
    left: 80px;
    top: 630px;
    background: var(--paper);
  }
  .person {
    position: absolute;
    left: 70px;
    top: 62px;
  }
  .person__name {
    font-size: 36px;
    font-weight: 400;
  }
  .person__name .accent { color: var(--brand-blue); }
  .person__role {
    font-size: 17px;
    margin-top: 2px;
  }
  .rule {
    position: absolute;
    left: 56px;
    width: 420px;
    height: 1.5px;
    background: var(--rule);
  }
  .rule--top { top: 150px; }
  .rule--bottom { top: 262px; }
  .contact {
    position: absolute;
    left: 56px;
    top: 172px;
    list-style: none;
  }
  .contact li {
    display: flex;
    align-items: center;
    gap: 16px;
    font-size: 21px;
    height: 38px;
  }
  .contact svg { width: 24px; height: 24px; flex: none; }
  .social {
    position: absolute;
    left: 56px;
    top: 284px;
    display: flex;
    gap: 44px;
    font-size: 19px;
  }
  .social__item { display: flex; align-items: center; gap: 10px; white-space: nowrap; }
  .social__dot { width: 22px; height: 22px; border-radius: 50%; flex: none; }
  .social__dot--a { background: var(--social-a); }
  .social__dot--b { background: var(--social-b); }
  .write-line {
    position: absolute;
    left: 56px;
    right: 56px;
    top: 380px;
    border-top: 1.5px dashed var(--dash);
  }
  .badge {
    position: absolute;
    right: 60px;
    top: 150px;
    width: 190px;
    height: 190px;
    border-radius: 50%;
    background: var(--brand-blue);
    color: #fff;
    font-weight: 700;
    font-size: 40px;
    letter-spacing: 0.06em;
    display: flex;
    align-items: center;
    justify-content: center;
  }
</style>
</head>
<body>

  <section class="card card--logo">
    <div class="brand-lockup">
      <span class="brand-lockup__dot"></span>
      <span class="brand-lockup__name">The Harbourline<br>Motion Clinic</span>
    </div>
  </section>

  <section class="card card--details">
    <div class="person">
      <p class="person__name">Name of <span class="accent">Person</span></p>
      <p class="person__role">Designation</p>
    </div>
    <div class="rule rule--top"></div>
    <ul class="contact">
      <li>
        <svg viewBox="0 0 24 24" aria-hidden="true"><circle cx="12" cy="12" r="10" fill="none" stroke="#111" stroke-width="2"/><path d="M9 7.5c-1.5 1.5-1.5 7.5 2 9.5l1.5-1.6-1.8-1.6c-.6-1-.6-2.7 0-3.6l1.8-1.6L11 6.8z" fill="#111"/></svg>
        <span>555.018.2046</span>
      </li>
      <li>
        <svg viewBox="0 0 24 24" aria-hidden="true"><rect x="2" y="5" width="20" height="14" fill="#111"/><path d="M2 5l10 8 10-8" fill="none" stroke="#fff" stroke-width="1.5"/></svg>
        <span>hello@harbourlinemotion.com</span>
      </li>
    </ul>
    <div class="rule rule--bottom"></div>
    <div class="social">
      <span class="social__item"><span class="social__dot social__dot--a"></span>social/harbourline</span>
      <span class="social__item"><span class="social__dot social__dot--b"></span>harbourline_motion</span>
    </div>
    <div class="write-line"></div>
    <div class="badge">THMC</div>
  </section>

</body>
</html>
```